Flyer needed to promote gutter clearance service for established gardening company

We need a bright and engaging flyer to be designed to advertise our gutter clearance service.
Whilst we are a gardening company that normally does more horticultural work, during the winter we offer other services such as gutter clearance where we remove the debris from gutters and thereby reducing the risk of clogs, leakage, breakage and potential structural damage to the property.

Full details of our service, together with our overall brand and colours can be seen on www.hartleyoutdoorcare.co.uk/gutters.

We would like you to use the page on the website as a basis to create the flyer and so please feel free to use as much or as little of the wording contained within the webpage on the flyer drawing particular attention to "Prices starting at just £60 for an average 3 bed house". I will upload pictures but please feel free to use other graphics and fonts to make it stand out.

The contact details which should be included within the flyer are as follows:

Hartley Outdoor Care Ltd
Kestrel Trade Park
Whitlow Moor Ind Estate
Swindon
SN3 7QL

Tel: 01793 418203
www.hartleyoutdoorcare.co.uk
mark@hartleyoutdoorcare.co.uk

The flyers will eventually be printed out in A5 (210mm x 148mm) using Printaloft and so needs to be in that size and suitable file for upload.

I have only put this as a 2 day project as its really urgent and I'm hoping we get some great designs in that time.

Target Market(s)

Homeowners between 25 - 65+

Industry/Entity Type

Home Improvement

Font styles to use
Serif
Sans Serif
Decorative
Script

Colors
6b449b
9bcb3c

Requirements
Must have
• Our colours are purple and green as seen on our website www.hartleyoutdoorcare.co.uk/gutters. Please use those colours.
• The flyer should draw attention to the following facts:
• We are Hartley Outdoor Care Ltd (see attached logo)
• We are offering a Gutter Clearance Service in Swindon
• Prices start at just £60 for the average 3 bed house.
• We are fully insured.
• Our contact details must be included (as in the product description above)
• I have attached pictures but feel free to add other graphics or use fonts to make the flyer more engaging and interesting.
• Additional wording may be taken from the website at the address shown above. You can use as much or as little wording as you like just as long as the message gets across and the flyer contains our contact information and logo and the details shown above.
Nice to have
• I would like a bright and modern design which isn't too busy or cluttered. It should be something that is quick and easy to read.
Should not have
• I don't want it to look too busy or crowded with small type which people just won't read. Whilst I've said you can take whatever wording you want from our website, I'd suggest you don't take it all or too much. I want the main message (as detailed above in 'must haves') to stand out rather than have it contained deep within lots of small type face.

```html
<!DOCTYPE html>
<html lang="en">
<head>
<meta charset="utf-8">
<title>Hartley Outdoor Care – Swindon Gutter Clearance</title>
<link href="https://fonts.googleapis.com/css2?family=Bebas+Neue&family=Luckiest+Guy&family=Nunito:ital,wght@0,700;0,800;1,800;1,900&family=Oswald:wght@500;600&display=swap" rel="stylesheet">
<style>
  :root {
    --purple: #6b449b;
    --purple-dark: #4e2f78;
    --green: #9bcb3c;
    --lime: #cfe02a;
    --leaf: #3cb54a;
    --red: #e01e26;
    --red-dark: #a9141a;
    --ink: #1b1b1b;
    --white: #ffffff;
  }
  * { box-sizing: border-box; margin: 0; padding: 0; }
  html, body { width: 846px; height: 1200px; overflow: hidden; background: var(--white); }
  .flyer { position: relative; width: 846px; height: 1200px; overflow: hidden; background: var(--white); font-family: "Nunito", sans-serif; }

  .panel-bg { position: absolute; left: 0; top: 0; width: 846px; height: 740px; }

  .brand { position: absolute; left: 46px; top: 60px; width: 360px; text-align: center; }
  .brand-mark { display: inline-block; width: 34px; height: 34px; border-radius: 50%; background: var(--green); margin-bottom: 10px; }
  .brand-name { font-family: "Nunito", sans-serif; font-weight: 800; font-size: 38px; line-height: 1.05; color: var(--purple); letter-spacing: 1px; }

  .photo { position: absolute; }
  .photo-hero { left: 474px; top: 20px; width: 319px; height: 400px; background: linear-gradient(160deg, #b3523b 0%, #8d5a45 30%, #2d3a5a 55%, #d9d3c7 80%, #a7a39c 100%); }
  .photo-before { left: 474px; top: 427px; width: 159px; height: 307px; background: linear-gradient(100deg, #6e6058 0%, #8a6a3e 40%, #a68850 60%, #e8e8e2 80%, #7fa04b 100%); }
  .photo-after { left: 639px; top: 427px; width: 154px; height: 307px; background: linear-gradient(100deg, #6b605a 0%, #8b8378 35%, #c7c5bd 60%, #eeeee9 80%, #7fa04b 100%); }
  .photo-label { position: absolute; top: 10px; font-family: "Luckiest Guy", sans-serif; font-size: 18px; color: var(--white); letter-spacing: 0.5px; -webkit-text-stroke: 1px #222; }
  .photo-before .photo-label { left: 84px; }
  .photo-after .photo-label { left: 90px; }

  .headline { position: absolute; left: 28px; top: 264px; }
  .headline-town { font-family: "Luckiest Guy", sans-serif; font-size: 58px; color: var(--lime); line-height: 1; letter-spacing: 1px; }
  .headline-service { font-family: "Bebas Neue", sans-serif; color: var(--white); font-size: 106px; line-height: 0.84; margin-top: 12px; }
  .price { position: absolute; left: 80px; top: 602px; display: flex; align-items: flex-end; }
  .price-lead { font-family: "Oswald", sans-serif; font-weight: 500; font-style: italic; color: var(--lime); line-height: 0.95; transform: skewX(-8deg); margin-right: 4px; margin-bottom: 12px; }
  .price-lead span { display: block; }
  .price-lead .small { font-size: 17px; }
  .price-lead .big { font-size: 30px; }
  .price-amount { font-family: "Nunito", sans-serif; font-weight: 900; font-style: italic; font-size: 84px; line-height: 0.85; color: var(--lime); letter-spacing: -2px; }
  .price-note { position: absolute; left: 42px; top: 682px; font-weight: 900; font-style: italic; font-size: 25px; color: var(--white); }

  .winter-band { position: absolute; left: 0; top: 738px; width: 846px; height: 150px; background: linear-gradient(180deg, var(--red-dark) 0%, var(--red) 8%, var(--red) 88%, var(--red-dark) 100%); border-top: 3px solid #7d0f12; border-bottom: 3px solid #7d0f12; }
  .insured { position: absolute; left: 14px; top: 730px; width: 380px; height: 170px; }
  .insured svg { position: absolute; left: 0; top: 0; width: 380px; height: 170px; }
  .insured-text { position: absolute; left: 0; top: 50px; width: 380px; text-align: center; }
  .insured-title { font-weight: 800; font-size: 26px; color: var(--purple); line-height: 1; }
  .insured-sub { font-weight: 700; font-size: 14.5px; color: #333; line-height: 1.3; margin-top: 4px; }
  .winter-call { position: absolute; left: 394px; top: 756px; width: 440px; text-align: center; font-family: "Bebas Neue", sans-serif; color: var(--lime); -webkit-text-stroke: 1px #6d6a10; }
  .winter-call .line-1 { font-size: 52px; line-height: 1; letter-spacing: 0.5px; }
  .winter-call .line-2 { font-size: 80px; line-height: 0.9; letter-spacing: 1px; }

  .contact { position: absolute; left: 0; top: 888px; width: 846px; height: 158px; }
  .photo-gloves { position: absolute; left: 373px; top: 0; width: 473px; height: 158px; background: linear-gradient(90deg, #ffffff 0%, rgba(255,255,255,0.6) 18%, #9ab06a 45%, #3f8f7e 70%, #2d4a2a 100%); }
  .contact-cta { position: absolute; left: 34px; top: 20px; font-family: "Bebas Neue", sans-serif; font-size: 36px; color: var(--ink); line-height: 1; }
  .contact-cta strong { color: var(--purple); font-weight: normal; font-size: 42px; }
  .contact-phone { position: absolute; left: 32px; top: 56px; font-family: "Bebas Neue", sans-serif; font-size: 90px; line-height: 0.85; color: var(--purple); letter-spacing: 1px; }
  .contact-links { position: absolute; left: 34px; top: 128px; font-family: "Oswald", sans-serif; font-weight: 600; font-size: 17px; color: #2b1a10; white-space: nowrap; }
  .contact-links .email { color: var(--purple); font-size: 15px; margin-left: 10px; }

  .clients-strip { position: absolute; left: 0; top: 1046px; width: 846px; height: 124px; background: var(--purple); }
  .clients-note { position: absolute; left: 0; top: 0; height: 25px; width: 620px; background: var(--lime); clip-path: polygon(0 0, 100% 0, 96% 100%, 0 100%); font-family: "Oswald", sans-serif; font-weight: 500; font-size: 15.5px; color: var(--purple); line-height: 25px; padding-left: 38px; }
  .service-list { position: absolute; left: 34px; top: 36px; width: 800px; display: grid; grid-template-columns: 201px 239px 219px 140px; row-gap: 6px; list-style: none; }
  .service-list li { font-family: "Oswald", sans-serif; font-weight: 600; font-size: 17px; color: var(--lime); line-height: 22px; padding-left: 22px; position: relative; white-space: nowrap; }
  .service-list li::before { content: ""; position: absolute; left: 0; top: 6px; width: 11px; height: 11px; border: 1.5px solid var(--white); }
  .service-list li::after { content: ""; position: absolute; left: 4px; top: 4px; width: 5px; height: 10px; border-right: 2px solid var(--white); border-bottom: 2px solid var(--white); transform: rotate(40deg); }

  .address-bar { position: absolute; left: 0; top: 1170px; width: 846px; height: 30px; background: var(--leaf); font-weight: 800; font-size: 15.5px; color: var(--white); line-height: 30px; text-align: center; }
  .address-bar .company { color: var(--lime); }
</style>
</head>
<body>
<div class="flyer">

  <svg class="panel-bg" viewBox="0 0 846 740" aria-hidden="true">
    <polygon points="0,260 463,207 463,734 0,734" fill="var(--purple)"/>
    <polygon points="0,254 463,202 463,208 0,261" fill="var(--leaf)"/>
    <polygon points="807,0 846,0 846,734 807,734" fill="var(--purple)"/>
    <polygon points="812,0 846,0 846,18 812,18" fill="var(--leaf)"/>
    <polygon points="807,0 846,0 807,18" fill="var(--white)"/>
  </svg>

  <div class="brand">
    <span class="brand-mark"></span>
    <div class="brand-name">Hartley Outdoor Care</div>
  </div>

  <div class="photo photo-hero" role="img" aria-label="Photo of a worker in ear defenders and safety glasses blowing autumn leaves out of a roof gutter"></div>
  <div class="photo photo-before" role="img" aria-label="Photo of a gutter clogged with leaves and debris"><span class="photo-label">Before</span></div>
  <div class="photo photo-after" role="img" aria-label="Photo of the same gutter cleared and clean"><span class="photo-label">After</span></div>

  <div class="headline">
    <div class="headline-town">SWINDON</div>
    <h1 class="headline-service">GUTTER<br>CLEARANCE<br>SERVICES</h1>
  </div>
  <div class="price">
    <div class="price-lead"><span class="small">STARTING</span><span class="big">FROM</span></div>
    <div class="price-amount">£60</div>
  </div>
  <div class="price-note">for the average 3 bed house</div>

  <div class="winter-band"></div>
  <div class="insured">
    <svg viewBox="-190 -85 380 170" aria-hidden="true">
      <polygon fill="var(--white)" stroke="var(--purple)" stroke-width="3" points="180,0 137.3,10.9 166.3,30.6 116.3,31.1 127.3,56.6 77.8,46.5 68.9,73.9 27.3,54.9 0,80 -27.3,54.9 -68.9,73.9 -77.8,46.5 -127.3,56.6 -116.3,31.1 -166.3,30.6 -137.3,10.9 -180,0 -137.3,-10.9 -166.3,-30.6 -116.3,-31.1 -127.3,-56.6 -77.8,-46.5 -68.9,-73.9 -27.3,-54.9 0,-80 27.3,-54.9 68.9,-73.9 77.8,-46.5 127.3,-56.6 116.3,-31.1 166.3,-30.6 137.3,-10.9"/>
    </svg>
    <div class="insured-text">
      <div class="insured-title">FULLY INSURED</div>
      <div class="insured-sub">using the latest tools and techniques<br>to safely clear your gutters</div>
    </div>
  </div>
  <div class="winter-call">
    <div class="line-1">GET YOUR HOME PREPARED</div>
    <div class="line-2">FOR THE WINTER</div>
  </div>

  <div class="contact">
    <div class="photo-gloves" role="img" aria-label="Photo of gloved hands clearing leaves from a gutter"></div>
    <div class="contact-cta">CALL FOR YOUR <strong>FREE</strong> QUOTE</div>
    <div class="contact-phone">01793 418 203</div>
    <div class="contact-links">www.hartleyoutdoorcare.co.uk <span>-</span><span class="email">mark@hartleyoutdoorcare.co.uk</span></div>
  </div>

  <div class="clients-strip">
    <div class="clients-note">OUR SERVICES ARE AVAILABLE TO BOTH DOMESTIC AND COMMERCIAL CLIENTS OF ALL SIZES</div>
    <ul class="service-list">
      <li>FENCING</li><li>GUTTER CLEARANCE</li><li>LAWN MOWING</li><li>TURFING</li>
      <li>HEDGE CUTTING</li><li>LAWN TREATMENTS</li><li>PLANTING &amp; DESIGN</li><li>TREE PRUNING</li>
      <li>GARDEN TIDY UP</li><li>REGULAR MAINTENANCE</li><li>SHRUB PRUNING</li><li>WEED KILLING</li>
    </ul>
  </div>

  <div class="address-bar"><span class="company">Hartley Outdoor Care Ltd,</span> Kestrel Trade Park, Whitlow Moor Ind Estate, Swindon, SN3 7QL</div>

</div>
</body>
</html>
```